Feeling Wheel Infographic

We need the 2 pptx mock-ups turned to 2 infographics. please add the logo to the infographics. The colours used on the mock-ups are example colours and can be changed - a gradient scale or the colours used on the mock-up would be great!

```html
<!DOCTYPE html>
<html lang="en">
<head>
<meta charset="utf-8">
<title>Feeling Wheel</title>
<link rel="stylesheet" href="https://fonts.googleapis.com/css2?family=Poppins:ital,wght@0,400;0,500;0,600;0,700;1,800&display=swap">
<style>
  :root {
    --bg: #f4f4f4;
    --ink: #111111;
    --ink-soft: #4a4a4a;
    --ring: #222222;
    --white: #ffffff;
    --red: #e8222e;
    --red-soft: #f27a85;
    --orange: #f47b20;
    --orange-soft: #f9a35c;
    --yellow: #f2e51d;
    --yellow-soft: #f6ee70;
    --green: #8cc63f;
    --green-soft: #c3dc84;
    --blue: #2a78c2;
    --blue-soft: #7fbbe8;
    --purple: #6a4fa8;
    --purple-soft: #8f82c8;
  }
  * { margin: 0; padding: 0; box-sizing: border-box; }
  html, body { width: 1200px; height: 1200px; overflow: hidden; }
  body {
    background: radial-gradient(circle at 50% 30%, #ffffff 0%, var(--bg) 75%);
    font-family: "Poppins", sans-serif;
    color: var(--ink);
    position: relative;
  }
  .wheel { position: absolute; left: 0; top: 0; width: 1200px; height: 1200px; }
  .wheel-ring { fill: var(--white); stroke: var(--ring); stroke-width: 1.6; }
  .wheel-arrow { fill: none; stroke: var(--ring); stroke-width: 2; }
  .arrow-head { fill: var(--ring); }
  .wheel-hub { fill: var(--white); }
  .hub-label { font-family: "Poppins", sans-serif; font-weight: 700; font-size: 26px; fill: #666666; text-anchor: middle; }
  .segment { stroke: var(--white); stroke-width: 3; stroke-linejoin: round; }
  .soft-red { fill: var(--red-soft); }
  .soft-orange { fill: var(--orange-soft); }
  .soft-yellow { fill: var(--yellow-soft); }
  .soft-green { fill: var(--green-soft); }
  .soft-blue { fill: var(--blue-soft); }
  .soft-purple { fill: var(--purple-soft); }
  .core-red { fill: var(--red); }
  .core-orange { fill: var(--orange); }
  .core-yellow { fill: var(--yellow); }
  .core-green { fill: var(--green); }
  .core-blue { fill: var(--blue); }
  .core-purple { fill: var(--purple); }
  .word { font-family: "Poppins", sans-serif; text-anchor: middle; font-weight: 400; }
  .word-outer { font-size: 14px; }
  .word-inner { font-size: 12.5px; }
  .text-light .word { fill: var(--white); }
  .text-dark .word { fill: var(--ink-soft); }
  .text-light .word-rule { stroke: rgba(255,255,255,0.85); }
  .text-dark .word-rule { stroke: rgba(80,80,80,0.6); }
  .word-rule { stroke-width: 1.2; }
  .core-label { font-family: "Poppins", sans-serif; font-weight: 700; font-size: 13px; text-anchor: middle; dominant-baseline: central; }
  .core-light { fill: var(--white); }
  .core-dark { fill: var(--ink); }

  .title {
    position: absolute; left: 796px; top: 292px;
    font-weight: 800; font-style: italic; font-size: 60px; line-height: 58px;
    letter-spacing: 0.5px; color: var(--ink);
  }
  .legend {
    position: absolute; left: 830px; top: 470px;
    display: grid; grid-template-columns: 90px 40px 120px;
    column-gap: 14px; row-gap: 13px; align-items: center;
    font-weight: 600; font-size: 17px; color: #222222;
  }
  .legend-left { text-align: right; }
  .legend-swatch { width: 40px; height: 40px; }
  .sw-red { background: var(--red); }
  .sw-purple { background: var(--purple); }
  .sw-blue { background: var(--blue); }
  .sw-green { background: var(--green); }
  .sw-yellow { background: var(--yellow); }
  .sw-orange { background: var(--orange); }
</style>
</head>
<body>

<svg class="wheel" viewBox="0 0 1200 1200" aria-label="Feeling wheel chart">
  <defs>
    <path id="outer-segment" d="M -34.7,-129.4 L -78.9,-294.6 A 305 305 0 0 1 78.9,-294.6 L 34.7,-129.4 A 134 134 0 0 0 -34.7,-129.4 Z"/>
    <path id="core-segment" d="M -13.5,-50.2 L -33.6,-125.6 A 130 130 0 0 1 33.6,-125.6 L 13.5,-50.2 A 52 52 0 0 0 -13.5,-50.2 Z"/>
    <marker id="arrow-tip" viewBox="0 0 10 10" refX="8" refY="5" markerWidth="7" markerHeight="7" orient="auto-start-reverse">
      <path class="arrow-head" d="M0,0 L10,5 L0,10 Z"/>
    </marker>
  </defs>

  <path class="wheel-arrow" d="M 289,288 A 350 350 0 0 1 617,288" marker-start="url(#arrow-tip)" marker-end="url(#arrow-tip)"/>
  <path class="wheel-arrow" d="M 289,906 A 350 350 0 0 0 617,906" marker-start="url(#arrow-tip)" marker-end="url(#arrow-tip)"/>

  <circle class="wheel-ring" cx="453" cy="597" r="316"/>

  <g transform="translate(453 597)">

    <!-- Angry -->
    <g transform="rotate(-15)">
      <use href="#outer-segment" class="segment soft-red"/>
      <use href="#core-segment" class="segment core-red"/>
      <g class="text-light">
        <text class="word word-outer" y="-264">Aggravated</text>
        <text class="word word-outer" y="-245">Irritated</text>
        <text class="word word-outer" y="-226">Jealous</text>
        <line class="word-rule" x1="-26" x2="26" y1="-212" y2="-212"/>
        <text class="word word-inner" y="-196">Frustrated</text>
        <text class="word word-inner" y="-180">Upset</text>
      </g>
      <text class="core-label core-light" transform="translate(0 -91) rotate(90)">Angry</text>
    </g>

    <!-- Proud -->
    <g transform="rotate(15)">
      <use href="#outer-segment" class="segment soft-orange"/>
      <use href="#core-segment" class="segment core-orange"/>
      <g class="text-light">
        <text class="word word-outer" y="-264">Brave</text>
        <text class="word word-outer" y="-245">Empowered</text>
        <text class="word word-outer" y="-226">Fulfilled</text>
        <line class="word-rule" x1="-26" x2="26" y1="-212" y2="-212"/>
        <text class="word word-inner" y="-196">Confident</text>
        <text class="word word-inner" y="-180">Encouraged</text>
      </g>
      <text class="core-label core-dark" transform="translate(0 -91) rotate(-90)">Proud</text>
    </g>

    <!-- Joyful -->
    <g transform="rotate(45)">
      <use href="#outer-segment" class="segment soft-yellow"/>
      <use href="#core-segment" class="segment core-yellow"/>
      <g class="text-dark">
        <text class="word word-outer" y="-264">Ecstatic</text>
        <text class="word word-outer" y="-245">Elated</text>
        <text class="word word-outer" y="-226">Thrilled</text>
        <line class="word-rule" x1="-26" x2="26" y1="-212" y2="-212"/>
        <text class="word word-inner" y="-196">Excited</text>
        <text class="word word-inner" y="-180">Happy</text>
      </g>
      <text class="core-label core-dark" transform="translate(0 -91) rotate(-90)">Joyful</text>
    </g>

    <!-- Intrigued -->
    <g transform="rotate(75)">
      <use href="#outer-segment" class="segment soft-green"/>
      <use href="#core-segment" class="segment core-green"/>
      <g class="text-dark">
        <text class="word word-outer" y="-264">Captivated</text>
        <text class="word word-outer" y="-245">Invested</text>
        <text class="word word-outer" y="-226">Fascinated</text>
        <line class="word-rule" x1="-26" x2="26" y1="-212" y2="-212"/>
        <text class="word word-inner" y="-196">Curious</text>
        <text class="word word-inner" y="-180">Engaged</text>
      </g>
      <text class="core-label core-dark" transform="translate(0 -91) rotate(-90)">Intrigued</text>
    </g>

    <!-- Trusting -->
    <g transform="rotate(105)">
      <use href="#outer-segment" class="segment soft-blue"/>
      <use href="#core-segment" class="segment core-blue"/>
      <text class="core-label core-light" transform="translate(0 -91) rotate(-90)">Trusting</text>
    </g>
    <g class="text-light" transform="rotate(-75)">
      <text class="word word-inner" y="184">Secure</text>
      <text class="word word-inner" y="200">Optimistic</text>
      <line class="word-rule" x1="-26" x2="26" y1="210" y2="210"/>
      <text class="word word-outer" y="228">Positive</text>
      <text class="word word-outer" y="247">Certain</text>
      <text class="word word-outer" y="266">Convinced</text>
    </g>

    <!-- Loving -->
    <g transform="rotate(135)">
      <use href="#outer-segment" class="segment soft-purple"/>
      <use href="#core-segment" class="segment core-purple"/>
      <text class="core-label core-light" transform="translate(0 -91) rotate(-90)">Loving</text>
    </g>
    <g class="text-light" transform="rotate(-45)">
      <text class="word word-inner" y="184">Affectionate</text>
      <text class="word word-inner" y="200">Connected</text>
      <line class="word-rule" x1="-26" x2="26" y1="210" y2="210"/>
      <text class="word word-outer" y="228">Admiration</text>
      <text class="word word-outer" y="247">Adoration</text>
      <text class="word word-outer" y="266">Reverence</text>
    </g>

    <!-- Peaceful -->
    <g transform="rotate(165)">
      <use href="#outer-segment" class="segment soft-red"/>
      <use href="#core-segment" class="segment core-red"/>
      <text class="core-label core-light" transform="translate(0 -91) rotate(-90)">Peaceful</text>
    </g>
    <g class="text-light" transform="rotate(-15)">
      <text class="word word-inner" y="184">Relaxed</text>
      <text class="word word-inner" y="200">Content</text>
      <line class="word-rule" x1="-26" x2="26" y1="210" y2="210"/>
      <text class="word word-outer" y="228">Tranquil</text>
      <text class="word word-outer" y="247">Calm</text>
      <text class="word word-outer" y="266">Satisfied</text>
    </g>

    <!-- Ashamed -->
    <g transform="rotate(195)">
      <use href="#outer-segment" class="segment soft-orange"/>
      <use href="#core-segment" class="segment core-orange"/>
      <text class="core-label core-dark" transform="translate(0 -91) rotate(90)">Ashamed</text>
    </g>
    <g class="text-light" transform="rotate(15)">
      <text class="word word-inner" y="184">Guilty</text>
      <text class="word word-inner" y="200">Embarrassed</text>
      <line class="word-rule" x1="-26" x2="26" y1="210" y2="210"/>
      <text class="word word-outer" y="228">Mortified</text>
      <text class="word word-outer" y="247">Remorseful</text>
      <text class="word word-outer" y="266">Regretful</text>
    </g>

    <!-- Sad -->
    <g transform="rotate(225)">
      <use href="#outer-segment" class="segment soft-yellow"/>
      <use href="#core-segment" class="segment core-yellow"/>
      <text class="core-label core-dark" transform="translate(0 -91) rotate(90)">Sad</text>
    </g>
    <g class="text-dark" transform="rotate(45)">
      <text class="word word-inner" y="184">Lonely</text>
      <text class="word word-inner" y="200">Disappointed</text>
      <line class="word-rule" x1="-26" x2="26" y1="210" y2="210"/>
      <text class="word word-outer" y="228">Isolated</text>
      <text class="word word-outer" y="247">Powerless</text>
      <text class="word word-outer" y="266">Heartbroken</text>
    </g>

    <!-- Surprised -->
    <g transform="rotate(255)">
      <use href="#outer-segment" class="segment soft-green"/>
      <use href="#core-segment" class="segment core-green"/>
      <text class="core-label core-dark" transform="translate(0 -91) rotate(90)">Surprised</text>
    </g>
    <g class="text-dark" transform="rotate(75)">
      <text class="word word-inner" y="184">Amazed</text>
      <text class="word word-inner" y="200">Confused</text>
      <line class="word-rule" x1="-26" x2="26" y1="210" y2="210"/>
      <text class="word word-outer" y="228">Startled</text>
      <text class="word word-outer" y="247">Shocked</text>
      <text class="word word-outer" y="266">Stunned</text>
    </g>

    <!-- Afraid -->
    <g transform="rotate(285)">
      <use href="#outer-segment" class="segment soft-blue"/>
      <use href="#core-segment" class="segment core-blue"/>
      <g class="text-light">
        <text class="word word-outer" y="-264">Worried</text>
        <text class="word word-outer" y="-245">Frightened</text>
        <text class="word word-outer" y="-226">Terrified</text>
        <line class="word-rule" x1="-26" x2="26" y1="-212" y2="-212"/>
        <text class="word word-inner" y="-196">Scared</text>
        <text class="word word-inner" y="-180">Nervous</text>
      </g>
      <text class="core-label core-light" transform="translate(0 -91) rotate(90)">Afraid</text>
    </g>

    <!-- Disgusted -->
    <g transform="rotate(315)">
      <use href="#outer-segment" class="segment soft-purple"/>
      <use href="#core-segment" class="segment core-purple"/>
      <g class="text-light">
        <text class="word word-outer" y="-264">Mortified</text>
        <text class="word word-outer" y="-245">Revolted</text>
        <text class="word word-outer" y="-226">Repulsed</text>
        <line class="word-rule" x1="-26" x2="26" y1="-212" y2="-212"/>
        <text class="word word-inner" y="-196">Appalled</text>
        <text class="word word-inner" y="-180">Sickened</text>
      </g>
      <text class="core-label core-light" transform="translate(0 -91) rotate(90)">Disgusted</text>
    </g>

    <circle class="wheel-hub" r="50"/>
    <text class="hub-label" y="9">logo</text>
  </g>
</svg>

<h1 class="title">FEELING<br>WHEEL</h1>

<div class="legend">
  <span class="legend-left">Angry</span><span class="legend-swatch sw-red"></span><span>Peaceful</span>
  <span class="legend-left">Disgusted</span><span class="legend-swatch sw-purple"></span><span>Loving</span>
  <span class="legend-left">Afraid</span><span class="legend-swatch sw-blue"></span><span>Trusting</span>
  <span class="legend-left">Surprised</span><span class="legend-swatch sw-green"></span><span>Intrigued</span>
  <span class="legend-left">Sad</span><span class="legend-swatch sw-yellow"></span><span>Joyful</span>
  <span class="legend-left">Ashamed</span><span class="legend-swatch sw-orange"></span><span>Proud</span>
</div>

</body>
</html>
```